Business card for Chiropractic clinics needs reworked / redesigned

The business card in attachment was designed 10 years ago. It is in need of an update.
We have 2 clinics:
VELDHOVE KLINIEK & VELDHOVE KLINIEK NOORD
Only one address needs to be on the card for doctors that only work in one clinic and two addresses need to be on the card for the doctors that work in both clinics.

Target Market(s)

patients/referrers

Industry/Entity Type

Medical

Contact Information for Business Card

Logo (in full or zoomed-in)
Clinic Name
Doctor name and title
clinic address, website, tel, email

Font styles to use
Sans Serif

Colors

Designer to choose colors to be used in the design.

Requirements
Must have
• Good contrast/readability
• We like modern minimalistic designs
• The Bcard needs to project our very high standard of proficiency/professionalism
Should not have
• Not curly
• Not to much colours

```html
<!DOCTYPE html>
<html lang="nl">
<head>
<meta charset="utf-8">
<title>Veldhove Kliniek – visitekaartje</title>
<link href="https://fonts.googleapis.com/css2?family=Questrial&display=swap" rel="stylesheet">
<style>
  :root {
    --backdrop: #d8dadb;
    --brand-green: #9bd063;
    --ink-green: #86c450;
    --rule-green: #b5dc8c;
    --paper: #f7f7f5;
    --white: #ffffff;
  }
  * { box-sizing: border-box; margin: 0; padding: 0; }
  html, body {
    width: 1200px; height: 857px; overflow: hidden;
    background: var(--backdrop);
    font-family: "Questrial", "Century Gothic", sans-serif;
  }
  .sheet {
    width: 1200px; height: 857px;
    display: flex; align-items: center; justify-content: center; gap: 40px;
  }
  .card {
    width: 540px; height: 309px;
    position: relative;
    box-shadow: 0 6px 18px rgba(0,0,0,.12);
  }
  .card--front {
    background: var(--brand-green);
    display: flex; flex-direction: column; align-items: center; justify-content: center;
    gap: 26px;
  }
  .brand-mark {
    width: 110px; height: 110px;
    border: 2px solid var(--white);
  }
  .brand-name {
    color: var(--white);
    font-size: 34px; letter-spacing: 3px;
  }
  .card--back {
    background: var(--paper);
    color: var(--ink-green);
    padding: 40px 44px 0 44px;
  }
  .doctor {
    margin-left: 150px;
    width: 280px;
  }
  .doctor__name { font-size: 27px; line-height: 1.1; }
  .doctor__title {
    font-size: 11px; letter-spacing: 1.5px;
    text-align: right; margin-top: 2px; margin-right: 28px;
  }
  .clinics {
    display: flex; gap: 26px; margin-top: 18px;
  }
  .clinic { width: 210px; font-size: 16.5px; line-height: 1.2; }
  .clinic--main { margin-top: 48px; }
  .clinic__name {
    font-size: 15px; letter-spacing: .3px;
    border-bottom: 1.5px solid var(--rule-green);
    padding-bottom: 3px; margin-bottom: 6px;
  }
</style>
</head>
<body>
<main class="sheet">
  <section class="card card--front" aria-label="Voorzijde visitekaartje">
    <div class="brand-mark" aria-hidden="true"></div>
    <p class="brand-name">VELDHOVE KLINIEK</p>
  </section>

  <section class="card card--back" aria-label="Achterzijde visitekaartje">
    <div class="doctor">
      <p class="doctor__name">Pieter Vandamme</p>
      <p class="doctor__title">CHIROPRACTOR</p>
    </div>
    <div class="clinics">
      <address class="clinic clinic--main" style="font-style:normal">
        <p class="clinic__name">VELDHOVE KLINIEK</p>
        <p>Kerkdreef 41</p>
        <p>09 555 01 24</p>
        <p>veldhovekliniek.be</p>
      </address>
      <address class="clinic clinic--north" style="font-style:normal">
        <p class="clinic__name">VELDHOVE KLINIEK NOORD</p>
        <p>Molenweg 17</p>
        <p>09 555 03 86</p>
        <p>veldhovenoord.be</p>
      </address>
    </div>
  </section>
</main>
</body>
</html>
```